new business card, with new logo. Looking for full design

I would like to have a graphic designer/artist create a high standard, premium business logo and business card design that I can either use to print on my own or have printed through them as well. Also, would be nice if I could customize with new employee names and info afterwards. Also, though I don't have a logo, something that matches the theme here https://larkfieldstrategyadvisors.com/ as well as incorporates the letter "M" is what I am currently thinking. Thanks!

Target Market(s)

High end corporate executives

Industry/Entity Type

Economics

Contact Information for Business Card

Dr. Oscar Teodoro-Lindqvist
Principal Advisor
OTL@LarkfieldStrategyAdvisors.com
other contact/website details from here: https://larkfieldstrategyadvisors.com/

Logo Text

Larkfield Strategy Advisors

```html
<!DOCTYPE html>
<html lang="en">
<head>
<meta charset="utf-8">
<title>Larkfield Strategy Advisors – Business Card</title>
<link rel="stylesheet" href="https://fonts.googleapis.com/css2?family=EB+Garamond:wght@400;500;700&display=swap">
<style>
  :root {
    --backdrop: #2a2a2a;
    --card: #1c1c1c;
    --rose: #d79c8c;
    --ink-light: #e9e6e3;
    --divider: #4a4a4a;
  }
  * { margin: 0; padding: 0; box-sizing: border-box; }
  html, body {
    width: 1200px; height: 900px; overflow: hidden;
    background: var(--backdrop);
    font-family: "EB Garamond", Georgia, serif;
  }
  .canvas {
    position: relative; width: 1200px; height: 900px;
    display: flex; flex-direction: column; align-items: center; justify-content: center; gap: 50px;
  }
  .card {
    width: 560px; height: 320px;
    background: var(--card);
    box-shadow: 0 10px 28px rgba(0,0,0,.45);
    position: relative;
  }
  .brand-mark {
    width: 40px; height: 40px;
    border: 2px solid var(--rose);
    flex: none;
  }
  .brand-name { color: var(--rose); font-weight: 400; }

  /* Front */
  .card-front { display: flex; align-items: center; justify-content: center; }
  .card-front .brand { display: flex; align-items: center; gap: 16px; }
  .card-front .brand-name { font-size: 30px; letter-spacing: .5px; }

  /* Back */
  .card-back { display: flex; }
  .back-brand {
    width: 270px; display: flex; flex-direction: column; align-items: center; justify-content: center; gap: 18px;
  }
  .back-brand .brand-mark { width: 74px; height: 74px; }
  .back-brand .brand-name { font-size: 22px; text-align: center; line-height: 1.15; }
  .divider { width: 1px; background: var(--divider); margin: 48px 0; }
  .contact {
    flex: 1; padding: 62px 0 0 30px; color: var(--ink-light);
    font-size: 14.5px; line-height: 1.25;
  }
  .person-name { color: var(--rose); font-weight: 700; font-size: 19px; letter-spacing: .6px; text-transform: uppercase; }
  .person-title { margin-bottom: 14px; }
  .address { margin-bottom: 18px; }
  .contact-list { list-style: none; }
  .contact-list li { display: flex; align-items: center; gap: 10px; margin-bottom: 3px; }
  .contact-list svg { width: 14px; height: 14px; flex: none; }
</style>
</head>
<body>
<main class="canvas">
  <section class="card card-front">
    <div class="brand">
      <span class="brand-mark"></span>
      <span class="brand-name">Larkfield Strategy Advisors</span>
    </div>
  </section>

  <section class="card card-back">
    <div class="back-brand">
      <span class="brand-mark"></span>
      <span class="brand-name">Larkfield Strategy<br>Advisors</span>
    </div>
    <div class="divider"></div>
    <div class="contact">
      <p class="person-name">Henrik Calloway</p>
      <p class="person-title">Managing Director</p>
      <p class="address">4180 Ashgrove Ave Suite 210<br>Easton, MD 21601</p>
      <ul class="contact-list">
        <li>
          <svg viewBox="0 0 24 24" fill="none" stroke="var(--rose)" stroke-width="2.2"><path d="M5 3h4l2 5-2.5 1.5a11 11 0 0 0 6 6L16 13l5 2v4a2 2 0 0 1-2 2A16 16 0 0 1 3 5a2 2 0 0 1 2-2z"/></svg>
          555.010.4821
        </li>
        <li>
          <svg viewBox="0 0 24 24" fill="none" stroke="var(--rose)" stroke-width="2.2"><rect x="2" y="5" width="20" height="14"/><path d="M2 5l10 8 10-8"/></svg>
          info@LarkfieldStrategyAdvisors.com
        </li>
        <li>
          <svg viewBox="0 0 24 24" fill="none" stroke="var(--rose)" stroke-width="2"><circle cx="12" cy="12" r="10"/><path d="M2 12h20M12 2c3 3 3 17 0 20M12 2c-3 3-3 17 0 20"/></svg>
          www.larkfieldstrategyadvisors.com
        </li>
      </ul>
    </div>
  </section>
</main>
</body>
</html>
```